Music video company site re-design :-)

Hi guys,

I run a small music video production company called "Northgate Clip Works".

It's the new year and I'm hoping to update our website design, but am at a bit of a loss - which is where I'm desperately hoping you can help!

I need something cool and contemporary but not utterly terrifying/confusing that your average band manager/solo artist funding their own music video for the first time, won't be put off.

If you can check out our current website (http://www.NorthgateClipWorks.example) I think that would probably help :-)

Target Market(s)

Solo music artists and managers of small groups/bands.

Industry/Entity Type

It Company

Requirements
Must have
• Clear, cool but accessible.

I'll need to be able to embed Pixora videos from our Pixora-plus account into the pages...

http://www.pixora.example/framehousefilms

I'd also like to be able to optimise the site for search engines, so we'll need text and not images with text in them.

I'd also like to include or use images from our videos throughout the site, so if you can include as many of these as possible that would be great.

I've uploaded a zip file with them in, how they are used is up to you guys, but the more the merrier.
Should not have
• Images of cameras, lights, clapper boards etc...

No bloody Times New Roman unless you are really reinventing that wheel or trying to make it look like my nan made my website with clip art.

Also, no god damn emoticons ;-)

```html
<!DOCTYPE html>
<html lang="en">
<head>
<meta charset="utf-8">
<title>Northgate Clip Works – Music Video</title>
<link rel="stylesheet" href="https://fonts.googleapis.com/css2?family=Dosis:wght@400;700;800&family=Ubuntu:wght@400;500;700&display=swap">
<style>
  :root {
    --bg: #000000;
    --ink: #ffffff;
    --ink-soft: #dcdcdc;
    --accent: #f7a400;
    --accent-dim: #b3720f;
    --reel-red: #e0301a;
    --rule: #3a2a12;
    --splash-hot: #ff9a00;
    --splash-red: #d82a08;
    --splash-deep: #5a0a18;
    --reel-blue: #0c1a24;
  }
  * { margin: 0; padding: 0; box-sizing: border-box; }
  html, body { width: 1020px; height: 1200px; overflow: hidden; background: var(--bg); }
  body { position: relative; font-family: "Ubuntu", sans-serif; color: var(--ink); }

  .header-splash {
    position: absolute; left: 40px; top: 0; width: 980px; height: 540px;
    background:
      radial-gradient(ellipse 220px 160px at 190px 210px, rgba(120,10,40,.9), transparent 70%),
      radial-gradient(ellipse 300px 220px at 560px 150px, var(--splash-hot), transparent 75%),
      radial-gradient(ellipse 260px 240px at 330px 250px, var(--splash-red), transparent 75%),
      radial-gradient(ellipse 380px 260px at 700px 320px, rgba(120,50,0,.85), transparent 75%),
      radial-gradient(ellipse 200px 200px at 820px 120px, rgba(230,110,0,.8), transparent 75%);
  }
  .nav-column {
    position: absolute; left: 60px; top: 100px; width: 237px; height: 420px;
    background: linear-gradient(90deg, transparent, rgba(0,0,0,.45));
    border-right: 1px solid rgba(0,0,0,.5);
  }

  .site-title { position: absolute; font-family: "Dosis", sans-serif; font-weight: 800; text-transform: uppercase; color: var(--ink); letter-spacing: -0.5px; }
  .site-title--first { right: 750px; top: 146px; font-size: 44px; transform: rotate(-3deg); transform-origin: right center; }
  .site-title--second { left: 312px; top: 108px; font-size: 64px; transform: rotate(-4deg); transform-origin: left center; }

  .main-nav { position: absolute; right: 748px; top: 276px; list-style: none; text-align: right; }
  .main-nav li { height: 30px; font-size: 13px; font-weight: 700; text-transform: uppercase; color: var(--ink); }
  .main-nav .is-active { color: var(--accent); margin-right: -10px; }
  .main-nav .is-active::after { content: ""; display: inline-block; margin-left: 6px; border-left: 4px solid var(--accent); border-top: 3px solid transparent; border-bottom: 3px solid transparent; vertical-align: middle; }

  .showreel-label { position: absolute; left: 493px; top: 258px; font-family: "Dosis", sans-serif; font-size: 22px; color: var(--reel-red); letter-spacing: -0.5px; }
  .showreel-label strong { font-weight: 800; }
  .showreel-player {
    position: absolute; left: 476px; top: 301px; width: 391px; height: 220px;
    background:
      radial-gradient(ellipse 160px 60px at 195px 110px, rgba(60,140,220,.55), transparent 70%),
      linear-gradient(180deg, #1a2a36, var(--reel-blue) 75%, #05090d);
  }

  .content { position: absolute; left: 270px; top: 533px; width: 640px; }
  .content h1 { font-size: 24px; font-weight: 500; color: var(--accent); padding: 0 11px 10px; border-bottom: 1px solid var(--rule); }
  .content p { margin: 12px 11px 0; font-size: 12px; line-height: 19px; color: var(--ink-soft); }
  .content p + p { margin-top: 19px; }
  .content .lead { color: var(--ink); font-weight: 700; }

  .testimonial-still {
    position: absolute; left: 0; top: 850px; width: 360px; height: 285px;
    border-radius: 48% 52% 46% 54%;
    background: radial-gradient(ellipse at 50% 45%, #f4e6f2 0%, #c77a7a 40%, #5a2020 70%, transparent 78%);
  }
  .testimonial { position: absolute; left: 361px; top: 1024px; width: 540px; }
  .testimonial blockquote { font-size: 12px; line-height: 19px; font-weight: 700; color: var(--accent); }
  .testimonial cite { display: block; margin-top: 18px; text-align: right; font-style: normal; font-size: 12px; font-weight: 700; color: var(--accent-dim); }
</style>
</head>
<body>
  <div class="header-splash" role="img" aria-label="Orange and red paint splash artwork behind the header"></div>
  <div class="nav-column"></div>

  <div class="site-title site-title--first">Northgate</div>
  <div class="site-title site-title--second">Clip Works</div>

  <ul class="main-nav">
    <li>Home</li>
    <li class="is-active">Music Video</li>
    <li>Promo Feature</li>
    <li>Band Site Design</li>
    <li>Prices</li>
    <li>Contact Us</li>
  </ul>

  <div class="showreel-label">SHOWREEL <strong>2010</strong></div>
  <div class="showreel-player" role="img" aria-label="Showreel video still: a dancer against blue lights with the words fresh approach"></div>

  <main class="content">
    <h1>Music Video</h1>
    <p class="lead">Need a music video made? You're in the right place. Got a great idea for your video, or no idea at all and want to talk about it? You're definitely in the right place. Got all the talent in the world, but a budget that's tighter than a pair of tight pants living on tight street? You're still in the right place (pop over to our "prices" section for more info on our "Entry Level" offer)</p>
    <p>It can be scary calling a production company to get a quote (we've worked in them for years), some people expect to have their ideas sneered at by "experts", others expect to be quoted "ball park" figures so astronomical that they're going to burn up on re-entry.</p>
    <p>But terrible metaphors aside, the best thing to do is give us a call or drop us a line to chat about want you need, we won't bite and we want to help.</p>
    <p>It's tough at the moment – everywhere – so we want your video to be the very best it can be, and within your budget. That way you look good, which makes us look good. Simple.</p>
  </main>

  <div class="testimonial-still" role="img" aria-label="Video still of a recording artist in a white jacket, framed by a paint splash edge"></div>
  <div class="testimonial">
    <blockquote>"I have a great working relationship with NCW and remain continually impressed with their professionalism throughout any of my projects. They have always delivered the goods and within budget. Would definitely work with these nice people again and happily recommend them to anybody...."</blockquote>
    <cite>True Verse (Recording Artist/VerseHouseDotCom)</cite>
  </div>
</body>
</html>
```